Zia Bortolo's Cialdine

Looking for a packaging Label for Italian cookies. It has started with my great grandmothers Pizzelle recipe. Recipe has been in the family for over 100 years.
The packaging will be either clear plastic bags or Clear plastic hinged containers. Hoping for something elegant but traditional Italian. I have attached the company logo for color and idea possibilities
Would also like to give donation to helping animal foundations

Target Market(s)

Cookie lovers, coffee and tea drinkers, lighter alternative to heavy cookies

Requirements
Nice to have
• Family, Italian tradition

```html
<!DOCTYPE html>
<html lang="en">
<head>
<meta charset="utf-8">
<title>Zia Bortolo's Cialdine – Label</title>
<link href="https://fonts.googleapis.com/css2?family=Mr+Dafoe&family=Mrs+Saint+Delafield&family=Barlow:wght@500&display=swap" rel="stylesheet">
<style>
  :root {
    --backdrop: #e4e5e7;
    --label-white: #ffffff;
    --gold: #e0a22b;
    --script-orange: #f5a300;
    --ink: #111111;
  }
  html, body {
    margin: 0;
    padding: 0;
    width: 1200px;
    height: 1200px;
    overflow: hidden;
    background: var(--backdrop);
  }
  .label {
    display: block;
    width: 1200px;
    height: 1200px;
  }
  .label-disc { fill: var(--label-white); }
  .dotted-border {
    fill: none;
    stroke: var(--ink);
    stroke-width: 5;
    stroke-linecap: round;
    stroke-dasharray: 0 13;
  }
  .top-tab { fill: var(--gold); }
  .maker-name {
    font-family: "Mrs Saint Delafield", cursive;
    font-size: 84px;
    fill: var(--ink);
  }
  .product-name {
    font-family: "Mr Dafoe", cursive;
    font-size: 215px;
    fill: var(--script-orange);
  }
  .tagline-band { fill: var(--gold); }
  .tagline-text {
    font-family: "Barlow", sans-serif;
    font-weight: 500;
    font-size: 34px;
    letter-spacing: 3px;
    fill: var(--ink);
  }
  .tradition-text {
    font-family: "Barlow", sans-serif;
    font-weight: 500;
    font-size: 36px;
    letter-spacing: 3px;
    fill: var(--ink);
  }
</style>
</head>
<body>
<svg class="label" viewBox="0 0 1200 1200" xmlns="http://www.w3.org/2000/svg" role="img" aria-label="Zia Bortolo's Cialdine round packaging label">
  <defs>
    <clipPath id="disc-clip">
      <circle cx="600" cy="600" r="500"/>
    </clipPath>
    <path id="tradition-arc" d="M 173 600 A 427 427 0 0 0 1027 600"/>
  </defs>

  <circle class="label-disc" cx="600" cy="600" r="500"/>

  <g clip-path="url(#disc-clip)">
    <rect class="top-tab" x="470" y="90" width="260" height="300" role="img" aria-label="Decorative gold tab area"/>
  </g>

  <circle class="dotted-border" cx="600" cy="600" r="468"/>

  <text class="maker-name" x="600" y="305" text-anchor="middle">Zia Bortolo's</text>

  <text class="product-name" x="600" y="640" text-anchor="middle">Cialdine</text>

  <g class="tagline">
    <rect class="tagline-band" x="370" y="786" width="460" height="70"/>
    <text class="tagline-text" x="600" y="833" text-anchor="middle">THE FAMILY RECIPE</text>
  </g>

  <text class="tradition-text" text-anchor="middle">
    <textPath href="#tradition-arc" startOffset="50%">ITALIAN TRADITION</textPath>
  </text>
</svg>
</body>
</html>
```